Curriculum Card Design for Martial Arts System

We need an editable curriculum card design for a martial arts system. Would like to have our logo in background or highlighted on card. Each level will have their own separate card that can be printed onto a postcard sized paper (5x7 and 6x9). Each technique has three parts to it E, F, and S and would like them to be able to have a line or box which an instructor can initial or check next to each technique. Would like to have each curriculum card be straightforward with slight modern and futuristic touches similar to the emblem and logo.

Industry/Entity Type

Martial Art

Requirements
Must have
• Must be able to be edited as the curriculum techniques and moves may change or added/subracted.We are looking for something that is very easy to understand but also eye catching.
Should not have
• please Don't be boring in design.

```html
<!DOCTYPE html>
<html lang="en">
<head>
<meta charset="utf-8">
<title>Ascent Combat Systems – Level One Curriculum Card</title>
<link rel="stylesheet" href="https://fonts.googleapis.com/css2?family=Lato:ital,wght@0,400;0,700;0,900;1,400;1,700&family=Libre+Baskerville:wght@700&display=swap">
<style>
  :root {
    --ink: #050606;
    --teal-deep: #0b3335;
    --teal-mid: #175356;
    --teal-glow: #2a7376;
    --brand-teal: #3fc4c9;
    --white: #ffffff;
    --rule: rgba(255,255,255,0.85);
    --box-fill: rgba(255,255,255,0.08);
    --box-label: rgba(255,255,255,0.55);
    --text-dark: #111;
  }
  * { box-sizing: border-box; margin: 0; padding: 0; }
  html, body { width: 900px; height: 1200px; overflow: hidden; background: #ddd; }
  .card {
    position: relative; width: 900px; height: 1200px; overflow: hidden;
    background: radial-gradient(ellipse at 50% 62%, var(--teal-glow) 0%, var(--teal-mid) 30%, var(--teal-deep) 70%);
    font-family: "Lato", sans-serif;
  }
  .top-band { position: absolute; left: 0; top: 0; width: 900px; height: 470px; }
  .photo {
    position: absolute; left: 413px; top: 0; width: 487px; height: 300px;
    background: linear-gradient(160deg, #2a2a2a 0%, #9c9c9c 45%, #3a3a3a 75%, #0a0a0a 100%);
  }
  .brand { position: absolute; left: 60px; top: 40px; width: 340px; text-align: center; }
  .brand-disc {
    width: 190px; height: 190px; border-radius: 50%; margin: 0 auto 30px;
    background: var(--brand-teal);
  }
  .brand-name { color: var(--brand-teal); font-weight: 700; text-transform: uppercase; line-height: 1; }
  .brand-name .main { display: block; font-size: 50px; letter-spacing: 6px; }
  .brand-name .sub { display: block; font-size: 19px; letter-spacing: 7px; margin-top: 6px; }
  .level-pill {
    position: absolute; left: 527px; top: 350px; width: 285px; height: 48px;
    border-radius: 14px;
    background: linear-gradient(#ffffff, #d6d6d6 60%, #a9a9a9);
    font-family: "Libre Baskerville", serif; font-weight: 700; font-size: 33px;
    color: var(--text-dark); text-align: center; line-height: 50px; letter-spacing: 0.5px;
  }
  .section {
    position: absolute; left: 84px; width: 736px;
    border: 2px solid var(--white); border-radius: 14px; overflow: hidden;
  }
  .section-title {
    height: 48px; line-height: 48px; text-align: center;
    background: linear-gradient(#ffffff, #e8e8e8 50%, #b8b8b8);
    font-weight: 700; font-size: 25px; color: var(--text-dark); letter-spacing: 0.5px;
  }
  .technique-list { display: grid; grid-template-columns: 1fr 1fr; list-style: none; }
  .technique-list li {
    display: flex; align-items: center; justify-content: space-between;
    height: 44px; padding: 0 12px 0 24px;
    color: var(--white); font-style: italic; font-size: 22px;
    border-top: 1.5px solid var(--rule);
  }
  .technique-list li:nth-child(-n+2) { border-top: none; }
  .technique-list li:nth-child(odd) { border-right: 1.5px solid var(--rule); }
  .technique { white-space: nowrap; }
  .technique::before { content: "• "; font-style: normal; }
  .technique-list.bold li { font-weight: 700; height: 47px; }
  .sign-off { display: flex; gap: 4px; flex-shrink: 0; margin-left: 8px; }
  .check-box {
    width: 19px; height: 19px; border: 1.5px solid var(--white); border-radius: 3px;
    background: var(--box-fill);
    font-style: normal; font-weight: 700; font-size: 10px; line-height: 16px;
    text-align: center; color: var(--box-label);
  }
  .concept { top: 491px; }
  .offense { top: 659px; }
  .movement { top: 875px; }
  .defense { top: 990px; }
  .footer {
    position: absolute; left: 0; bottom: 0; width: 900px; height: 80px;
    background: linear-gradient(#bdbdbd, #f2f2f2 30%, #ffffff);
    text-align: center; line-height: 80px;
    font-weight: 700; font-size: 26px; letter-spacing: 11px; color: var(--text-dark);
  }
</style>
</head>
<body>
<main class="card">
  <svg class="top-band" viewBox="0 0 900 470" aria-hidden="true">
    <path d="M0 0 H900 V300 C760 300 640 330 520 380 C380 440 220 470 0 450 Z" fill="var(--ink)"/>
    <path d="M0 450 C220 470 380 440 520 380 C640 330 760 300 900 300" fill="none" stroke="#d4d4d4" stroke-width="6"/>
  </svg>
  <div class="photo" role="img" aria-label="Black and white photo of two martial artists in white uniforms sparring"></div>
  <svg class="top-band" viewBox="0 0 900 470" aria-hidden="true">
    <path d="M413 300 C560 290 700 260 900 275 V300 C760 300 640 330 520 380 Z" fill="var(--ink)"/>
  </svg>

  <header class="brand">
    <div class="brand-disc"></div>
    <h1 class="brand-name"><span class="main">Ascent</span><span class="sub">Combat Systems</span></h1>
  </header>

  <div class="level-pill">LEVEL ONE</div>

  <section class="section concept">
    <h2 class="section-title">CONCEPT</h2>
    <ul class="technique-list">
      <li><span class="technique">Closed Stance</span><span class="sign-off"><span class="check-box">E</span><span class="check-box">F</span><span class="check-box">S</span></span></li>
      <li><span class="technique">Picture Frame Positioning</span><span class="sign-off"><span class="check-box">E</span><span class="check-box">F</span><span class="check-box">S</span></span></li>
      <li><span class="technique">Hand Positioning</span><span class="sign-off"><span class="check-box">E</span><span class="check-box">F</span><span class="check-box">S</span></span></li>
      <li><span class="technique">Point of Origin</span><span class="sign-off"><span class="check-box">E</span><span class="check-box">F</span><span class="check-box">S</span></span></li>
    </ul>
  </section>

  <section class="section offense">
    <h2 class="section-title">OFFENSE</h2>
    <ul class="technique-list">
      <li><span class="technique">Back Fist</span><span class="sign-off"><span class="check-box">E</span><span class="check-box">F</span><span class="check-box">S</span></span></li>
      <li><span class="technique">Step Drag Body Punch</span><span class="sign-off"><span class="check-box">E</span><span class="check-box">F</span><span class="check-box">S</span></span></li>
      <li><span class="technique">Body Punch</span><span class="sign-off"><span class="check-box">E</span><span class="check-box">F</span><span class="check-box">S</span></span></li>
      <li><span class="technique">Round Kick</span><span class="sign-off"><span class="check-box">E</span><span class="check-box">F</span><span class="check-box">S</span></span></li>
      <li><span class="technique">Step Drag Back Fist</span><span class="sign-off"><span class="check-box">E</span><span class="check-box">F</span><span class="check-box">S</span></span></li>
      <li><span class="technique">Side Kick</span><span class="sign-off"><span class="check-box">E</span><span class="check-box">F</span><span class="check-box">S</span></span></li>
    </ul>
  </section>

  <section class="section movement">
    <h2 class="section-title">MOVEMENT</h2>
    <ul class="technique-list bold">
      <li><span class="technique">Neutral Bounce</span><span class="sign-off"><span class="check-box">E</span><span class="check-box">F</span><span class="check-box">S</span></span></li>
      <li><span class="technique">Step Drag</span><span class="sign-off"><span class="check-box">E</span><span class="check-box">F</span><span class="check-box">S</span></span></li>
    </ul>
  </section>

  <section class="section defense">
    <h2 class="section-title">DEFENSE/COUNTERS</h2>
    <ul class="technique-list bold">
      <li><span class="technique">Wall Block</span><span class="sign-off"><span class="check-box">E</span><span class="check-box">F</span><span class="check-box">S</span></span></li>
      <li><span class="technique">Push Checks</span><span class="sign-off"><span class="check-box">E</span><span class="check-box">F</span><span class="check-box">S</span></span></li>
    </ul>
  </section>

  <footer class="footer">www.ascentcombat.com</footer>
</main>
</body>
</html>
```